Theatre Company needs a Poster design for a world premiere of "Ember Hollow" Play.

We are premiering a play that celebrates community in rural and regional Australia . We need a poster for A3 and A5 size and an image that can be used in our email correspondence/webpage.

Attached is some ideas the producing theatre committee has come up with, a river runs through the town itself.

Town

```html
<!DOCTYPE html>
<html lang="en">
<head>
<meta charset="utf-8">
<title>Ember Hollow – Poster</title>
<link rel="stylesheet" href="https://fonts.googleapis.com/css2?family=Bodoni+Moda:opsz,wght@6..96,700&family=Cormorant+Garamond:ital,wght@1,600&family=Great+Vibes&display=swap">
<style>
  :root {
    --ink: #000000;
    --paper: #ffffff;
    --sepia-light: #e6c99a;
    --sepia-mid: #a8814f;
    --sepia-dark: #3b2a18;
  }
  html, body {
    margin: 0;
    padding: 0;
    overflow: hidden;
    background: var(--ink);
  }
  .poster {
    position: relative;
    width: 939px;
    height: 1200px;
    background: var(--ink);
    color: var(--paper);
    overflow: hidden;
  }
  .company {
    position: absolute;
    top: 82px;
    left: 0;
    width: 100%;
    margin: 0;
    text-align: center;
    font-family: "Bodoni Moda", serif;
    font-weight: 700;
    font-size: 37px;
    letter-spacing: 3px;
    transform: scaleX(0.82);
  }
  .presents {
    position: absolute;
    top: 152px;
    left: 0;
    width: 100%;
    margin: 0;
    text-align: center;
    font-family: "Cormorant Garamond", serif;
    font-style: italic;
    font-weight: 600;
    font-size: 34px;
    letter-spacing: 9px;
  }
  .scene {
    position: absolute;
    left: 118px;
    top: 178px;
    width: 704px;
    height: 842px;
  }
  .title {
    position: absolute;
    top: 905px;
    left: 0;
    width: 100%;
    margin: 0;
    text-align: center;
    font-family: "Great Vibes", cursive;
    font-weight: 400;
    font-size: 150px;
    line-height: 1.2;
  }
  .credit {
    position: absolute;
    top: 1076px;
    left: 0;
    width: 100%;
    margin: 0;
    text-align: center;
    font-family: "Cormorant Garamond", serif;
    font-style: italic;
    font-weight: 600;
    font-size: 29px;
    letter-spacing: 2px;
  }
</style>
</head>
<body>
  <main class="poster">
    <p class="company">MARLOW BEND THEATRE COMPANY</p>
    <p class="presents">Presents</p>

    <svg class="scene" viewBox="0 0 704 842" role="img"
         aria-label="Sepia photograph of a treeline at dusk reflected in a still river, framed in a soft-edged oval">
      <defs>
        <linearGradient id="river-tones" x1="0" y1="0" x2="0" y2="1">
          <stop offset="0" stop-color="var(--sepia-dark)"/>
          <stop offset="0.25" stop-color="var(--sepia-mid)"/>
          <stop offset="0.45" stop-color="var(--sepia-light)"/>
          <stop offset="0.5" stop-color="var(--sepia-dark)"/>
          <stop offset="0.55" stop-color="var(--sepia-mid)"/>
          <stop offset="0.75" stop-color="var(--sepia-light)"/>
          <stop offset="1" stop-color="var(--sepia-dark)"/>
        </linearGradient>
        <filter id="soft-edge" x="-10%" y="-10%" width="120%" height="120%">
          <feGaussianBlur stdDeviation="14"/>
        </filter>
      </defs>
      <ellipse cx="352" cy="421" rx="338" ry="405" fill="url(#river-tones)" filter="url(#soft-edge)"/>
    </svg>

    <h1 class="title">Ember Hollow</h1>
    <p class="credit">Written by DANA WHITLOCK</p>
  </main>
</body>
</html>
```